Cricket Protein Balls- Packaging design

We are re-designing our current artwork for our protein balls made from cricket flour. Cricket flour is a sustainable and environmentally friendly source of protein. There are 2 varieties (so we will require 2 label designs)

Required on the label will be-

Our logo (see attached)
Name of product
A small section to one side to contain text (on one edge)- Exact text will be updated shortly. So please enter filler text until actual is supplied.

The first products name will be- Cacao, Cranberry & Chia Orvin Pops

The second variety is- Chilli & Lime Orvin Pops

Please do not include photographs of bugs on the label design. Silhouettes or drawings are OK.

The design will be for a label (sticker) which will be applied to the front of a curved deli cup container. The label design should be curved slightly to allow for bend in container. Approx dimensions will be 3cm (h) x 10cm (l)

Colours below are given as a guide only- please feel free to be creative if you have another colour pallet in mind

Target Market(s)

This product is aimed at consumers who are interested in the paleo diet, environmental issues and body builders (high protein).

Industry/Entity Type

Product

Colors
acd037
cadf82
faee3f
34b8a4
86cfc6
b7a5cd
8768ae

Requirements
Must have
• bright eye catching design with environmental/sustainable feel.

Text must be easy to read

```html
<!DOCTYPE html>
<html lang="en">
<head>
<meta charset="utf-8">
<title>Orvin Pops — Label Designs</title>
<link rel="stylesheet" href="https://fonts.googleapis.com/css2?family=Passion+One:wght@400;700&family=Open+Sans:wght@600;700&display=swap">
<style>
  :root {
    --bg-top: #ffffff;
    --bg-bottom: #e9e9ea;
    --purple: #9f6fb4;
    --purple-deep: #8a5aa3;
    --green: #8dbd3c;
    --green-deep: #78a82c;
    --white: #ffffff;
  }
  html, body {
    margin: 0;
    padding: 0;
    width: 1200px;
    height: 1200px;
    overflow: hidden;
  }
  body {
    background: radial-gradient(ellipse at 50% 40%, var(--bg-top) 0%, var(--bg-bottom) 100%);
    font-family: "Passion One", "Arial Black", sans-serif;
  }
  .canvas {
    position: relative;
    width: 1200px;
    height: 1200px;
  }
  .label {
    position: absolute;
    left: 80px;
    width: 1040px;
    height: 416px;
    filter: drop-shadow(0 8px 14px rgba(0,0,0,0.12));
  }
  .label--cacao { top: 150px; --tone: var(--purple); --tone-deep: var(--purple-deep); }
  .label--chilli { top: 640px; --tone: var(--green); --tone-deep: var(--green-deep); }

  .label__body { fill: var(--tone); }
  .label__panel { fill: var(--white); }
  .label__bite { fill: var(--tone); }
  .brand-name {
    fill: var(--white);
    font-family: "Passion One", "Arial Black", sans-serif;
    font-weight: 400;
    font-size: 38px;
  }
  .brand-dot { fill: var(--white); }
  .badge { fill: var(--white); }
  .flavour {
    fill: var(--tone);
    font-family: "Passion One", "Arial Black", sans-serif;
    font-weight: 400;
  }
  .product-name {
    fill: var(--white);
    font-family: "Passion One", "Arial Black", sans-serif;
    font-weight: 400;
    font-size: 64px;
  }
  .cricket { fill: var(--tone-deep); }
  .weight-disc { fill: var(--white); }
  .weight-value {
    fill: var(--tone);
    font-family: "Open Sans", Arial, sans-serif;
    font-weight: 700;
    font-size: 22px;
  }
  .ready {
    fill: var(--white);
    font-family: "Open Sans", Arial, sans-serif;
    font-weight: 600;
    font-size: 19px;
  }
  .ingredients {
    fill: var(--white);
    font-family: "Open Sans", Arial, sans-serif;
    font-weight: 600;
    font-size: 16px;
  }
  .ingredients__lead { font-weight: 700; }
</style>
</head>
<body>
<main class="canvas">

  <!-- Cacao, Cranberry & Chia label -->
  <svg class="label label--cacao" viewBox="0 0 1000 400" aria-label="Cacao, Cranberry and Chia Orvin Pops label">
    <path class="label__body" d="M20 60 Q500 -20 980 60 L940 390 Q500 320 60 390 Z"/>

    <g class="brand">
      <circle class="brand-dot" cx="100" cy="115" r="14"/>
      <text class="brand-name" x="80" y="170">HOPFIELD</text>
      <text class="brand-name" x="92" y="208">PANTRY</text>
    </g>
    <circle class="badge" cx="150" cy="295" r="36"/>

    <g class="panel">
      <path class="label__panel" d="M275 85 L740 65 L750 255 L282 268 Z"/>
      <circle class="label__bite" cx="700" cy="63" r="14"/>
      <circle class="label__bite" cx="726" cy="69" r="14"/>
      <circle class="label__bite" cx="748" cy="85" r="13"/>
    </g>

    <rect class="cricket" x="292" y="98" width="44" height="26" rx="10" role="img" aria-label="Cricket silhouette"/>
    <rect class="cricket" x="298" y="208" width="38" height="24" rx="10" role="img" aria-label="Cricket silhouette"/>
    <rect class="cricket" x="362" y="214" width="42" height="26" rx="10" role="img" aria-label="Cricket silhouette"/>

    <text class="flavour" x="355" y="138" font-size="58" textLength="230" lengthAdjust="spacingAndGlyphs">Cacao,</text>
    <text class="flavour" x="330" y="192" font-size="58" textLength="370" lengthAdjust="spacingAndGlyphs">Cranberry</text>
    <text class="flavour" x="420" y="246" font-size="36">&amp;</text>
    <text class="flavour" x="455" y="246" font-size="58" textLength="190" lengthAdjust="spacingAndGlyphs">Chia</text>

    <text class="product-name" x="292" y="324" textLength="440" lengthAdjust="spacingAndGlyphs">ORVIN POPS</text>

    <circle class="weight-disc" cx="805" cy="175" r="28"/>
    <text class="weight-value" x="805" y="183" text-anchor="middle">20g</text>
    <text class="ready" x="805" y="228" text-anchor="middle">Ready</text>
    <text class="ready" x="805" y="250" text-anchor="middle">to Eat</text>

    <g class="ingredients" transform="translate(872 320) rotate(-82)">
      <text y="0"><tspan class="ingredients__lead">Ingredients:</tspan> filler text until</text>
      <text y="21">final copy is supplied, filler</text>
      <text y="42">text until final copy.</text>
    </g>
  </svg>

  <!-- Chilli & Lime label -->
  <svg class="label label--chilli" viewBox="0 0 1000 400" aria-label="Chilli and Lime Orvin Pops label">
    <path class="label__body" d="M20 60 Q500 -20 980 60 L940 390 Q500 320 60 390 Z"/>

    <g class="brand">
      <circle class="brand-dot" cx="100" cy="115" r="14"/>
      <text class="brand-name" x="80" y="170">HOPFIELD</text>
      <text class="brand-name" x="92" y="208">PANTRY</text>
    </g>
    <circle class="badge" cx="150" cy="295" r="36"/>

    <g class="panel">
      <path class="label__panel" d="M275 85 L740 65 L750 255 L282 268 Z"/>
      <circle class="label__bite" cx="700" cy="63" r="14"/>
      <circle class="label__bite" cx="726" cy="69" r="14"/>
      <circle class="label__bite" cx="748" cy="85" r="13"/>
    </g>

    <rect class="cricket" x="372" y="92" width="44" height="28" rx="10" role="img" aria-label="Cricket silhouette"/>
    <rect class="cricket" x="660" y="158" width="42" height="26" rx="10" role="img" aria-label="Cricket silhouette"/>
    <rect class="cricket" x="328" y="212" width="40" height="26" rx="10" role="img" aria-label="Cricket silhouette"/>

    <text class="flavour" x="430" y="152" font-size="80" textLength="210" lengthAdjust="spacingAndGlyphs">Chilli</text>
    <text class="flavour" x="390" y="236" font-size="42">&amp;</text>
    <text class="flavour" x="438" y="236" font-size="80" textLength="230" lengthAdjust="spacingAndGlyphs">Lime</text>

    <text class="product-name" x="292" y="324" textLength="440" lengthAdjust="spacingAndGlyphs">ORVIN POPS</text>

    <circle class="weight-disc" cx="805" cy="175" r="28"/>
    <text class="weight-value" x="805" y="183" text-anchor="middle">20g</text>
    <text class="ready" x="805" y="228" text-anchor="middle">Ready</text>
    <text class="ready" x="805" y="250" text-anchor="middle">to Eat</text>

    <g class="ingredients" transform="translate(872 320) rotate(-82)">
      <text y="0"><tspan class="ingredients__lead">Ingredients:</tspan> filler text until</text>
      <text y="21">final copy is supplied, filler</text>
      <text y="42">text until final copy.</text>
    </g>
  </svg>

</main>
</body>
</html>
```